Business Card Design Project

I would like to get a logo as well as business card and stationery.

i am in an event planner and coordination business. I need something sophisticated and elegant.

Industry/Entity Type

Business

```html
<!DOCTYPE html>
<html lang="en">
<head>
<meta charset="utf-8">
<title>Aster Events NYC — Business Card</title>
<link rel="stylesheet" href="https://fonts.googleapis.com/css2?family=Open+Sans:wght@400;600;700&display=swap">
<style>
  :root {
    --canvas-bg: #ffffff;
    --ink: #111111;
    --ink-soft: #333333;
    --navy: #040a3c;
    --paper: #ffffff;
    --mark-grey: #333333;
  }
  html, body {
    margin: 0;
    padding: 0;
    width: 1200px;
    height: 708px;
    overflow: hidden;
    background: var(--canvas-bg);
  }
  .canvas {
    position: relative;
    width: 1200px;
    height: 708px;
    font-family: "Open Sans", Arial, sans-serif;
    color: var(--ink);
  }
  .side-label {
    position: absolute;
    font-size: 22px;
    font-weight: 400;
    color: var(--ink);
    transform: translateX(-50%);
    margin: 0;
    line-height: 1;
  }
  .side-label--front { left: 350px; top: 168px; }
  .side-label--back  { left: 949px; top: 36px; }

  /* Front of card */
  .card-front {
    position: absolute;
    left: 63px;
    top: 212px;
    width: 564px;
    height: 322px;
    background: var(--navy);
  }
  .brand-square {
    position: absolute;
    left: 25px;
    top: 218px;
    width: 77px;
    height: 77px;
    background: var(--paper);
  }
  .brand-name {
    position: absolute;
    left: 118px;
    top: 222px;
    margin: 0;
    font-size: 52px;
    font-weight: 600;
    line-height: 1;
    letter-spacing: -0.5px;
    color: var(--paper);
    white-space: nowrap;
  }

  /* Back of card */
  .card-back {
    position: absolute;
    left: 792px;
    top: 90px;
    width: 320px;
    height: 562px;
    border: 2px solid var(--ink);
    background: var(--paper);
    text-align: center;
  }
  .back-mark {
    position: absolute;
    left: 125px;
    top: 130px;
    width: 78px;
    height: 78px;
    background: var(--mark-grey);
  }
  .holder-name {
    position: absolute;
    left: 0;
    right: 0;
    top: 250px;
    margin: 0;
    font-size: 33px;
    font-weight: 700;
    line-height: 1;
    color: var(--ink);
  }
  .holder-role {
    position: absolute;
    left: 0;
    right: 0;
    top: 290px;
    margin: 0;
    font-size: 16px;
    font-weight: 700;
    line-height: 1;
    color: var(--ink);
  }
  .contact-list {
    position: absolute;
    left: 0;
    right: 0;
    top: 445px;
    margin: 0;
    padding: 0;
    list-style: none;
    font-size: 17px;
    font-weight: 700;
    line-height: 22.5px;
    color: var(--ink-soft);
  }
  .contact-city {
    font-size: 21px;
    line-height: 32px;
  }
</style>
</head>
<body>
  <main class="canvas">
    <p class="side-label side-label--front">Front</p>
    <section class="card-front" aria-label="Card front">
      <div class="brand-square" aria-hidden="true"></div>
      <h1 class="brand-name">aster events nyc</h1>
    </section>

    <p class="side-label side-label--back">Back</p>
    <section class="card-back" aria-label="Card back">
      <div class="back-mark" aria-hidden="true"></div>
      <h2 class="holder-name">Maren T. Holt</h2>
      <p class="holder-role">special event management</p>
      <ul class="contact-list">
        <li class="contact-phone">+1.555.014.2267</li>
        <li class="contact-email">maren@aster.com</li>
        <li class="contact-web">asterevnyc.com</li>
        <li class="contact-city">New York City</li>
      </ul>
    </section>
  </main>
</body>
</html>
```